Gin Bottle label design

A label for three Gins, 1 Apple flavoured, 1 Bilberry flavoured and one London Dry Gin. All need to incorporate the business logo that i've attached along with the bottle we intend to use. The gin is 40% and will be in a 70cl bottle

```html
<!DOCTYPE html>
<html lang="en">
<head>
<meta charset="utf-8">
<title>Gin Label – Apple Flavoured</title>
<link rel="stylesheet" href="https://fonts.googleapis.com/css2?family=Russo+One&family=Cabin:wght@600&family=Cinzel:wght@500&display=swap">
<style>
  :root {
    --page: #ffffff;
    --label-light: #fbf0e3;
    --label-mid: #f3dfc6;
    --label-edge: #ebcfad;
    --ink: #3a251a;
    --art-light: #eadac6;
    --art-mid: #d6bfa3;
    --art-dark: #bfa384;
  }
  html, body {
    margin: 0;
    width: 1200px;
    height: 1200px;
    overflow: hidden;
    background: var(--page);
  }
  .canvas {
    position: relative;
    width: 1200px;
    height: 1200px;
  }
  .gin-label {
    position: absolute;
    left: 190px;
    top: 70px;
    width: 820px;
    height: 1061px;
    display: block;
  }
  .frame-line { fill: none; stroke: var(--ink); stroke-width: 5; stroke-linecap: square; }
  .frame-thin { fill: none; stroke: var(--ink); stroke-width: 3.5; stroke-linecap: square; }
  .brand-dot { fill: none; stroke: var(--ink); stroke-width: 2.5; }
  .brand-name { font-family: "Cinzel", serif; font-weight: 500; font-size: 26px; fill: var(--ink); letter-spacing: 1px; }
  .product-name { font-family: "Russo One", sans-serif; font-size: 126px; fill: var(--ink); letter-spacing: 2px; }
  .product-flavour { font-family: "Cabin", sans-serif; font-weight: 600; font-size: 33px; fill: var(--ink); }
  .product-spec { font-family: "Cabin", sans-serif; font-weight: 600; fill: var(--ink); }
</style>
</head>
<body>
<main class="canvas">
  <svg class="gin-label" viewBox="0 0 728 942" xmlns="http://www.w3.org/2000/svg">
    <defs>
      <radialGradient id="labelTone" cx="50%" cy="52%" r="65%">
        <stop offset="0" stop-color="var(--label-light)"/>
        <stop offset="0.55" stop-color="var(--label-mid)"/>
        <stop offset="1" stop-color="var(--label-edge)"/>
      </radialGradient>
      <radialGradient id="artTone" cx="50%" cy="50%" r="55%">
        <stop offset="0" stop-color="var(--art-light)" stop-opacity="0.5"/>
        <stop offset="0.45" stop-color="var(--art-mid)" stop-opacity="0.75"/>
        <stop offset="0.8" stop-color="var(--art-dark)" stop-opacity="0.55"/>
        <stop offset="1" stop-color="var(--art-dark)" stop-opacity="0"/>
      </radialGradient>
    </defs>

    <rect class="label-ground" width="728" height="942" fill="url(#labelTone)"/>

    <!-- plain top frame -->
    <g class="frame-top">
      <path class="frame-line" d="M14 322 V30 H312"/>
      <path class="frame-line" d="M412 30 H710 V322"/>
      <path class="frame-line" d="M34 340 V50 H694 V340"/>
      <path class="frame-thin" d="M52 340 V68 H676 V340"/>
    </g>

    <!-- plain bottom frame -->
    <g class="frame-bottom">
      <path class="frame-line" d="M36 626 V912 H318"/>
      <path class="frame-line" d="M406 912 H692 V626"/>
      <path class="frame-line" d="M54 700 V884 H300"/>
      <path class="frame-line" d="M420 884 H674 V700"/>
    </g>

    <!-- brand name -->
    <g class="brand-mark">
      <circle class="brand-dot" cx="232" cy="196" r="12"/>
      <text class="brand-name" x="372" y="205" text-anchor="middle">THE OLIVE TABLE</text>
    </g>

    <!-- illustration area -->
    <rect class="botanical-art" x="56" y="300" width="618" height="370"
          fill="url(#artTone)" role="img"
          aria-label="Engraved illustration of apples hanging on a leafy branch"/>

    <!-- product text -->
    <text class="product-name" x="364" y="776" text-anchor="middle">GIN</text>
    <text class="product-flavour" x="364" y="820" text-anchor="middle">Apple Flavoured</text>
    <text class="product-spec" x="160" y="874" font-size="30">70cl</text>
    <text class="product-spec" x="565" y="874" text-anchor="end" font-size="24">40% alc.vol.</text>
  </svg>
</main>
</body>
</html>
```